Business card design for crowd sourced review site.

I need a business card magnet design for an online, crowd-sourced, restaurant review site strictly for Kosher restaurants.
It is similar to RoamLedger but catering to a very particular crowd.
The markets it will be distributed in are flooded with business card fridge magnets so this needs to be eye-catching and unique. The Business name is PlateMarks
The website isnt finished but you can see the basic setup here
http://restaurant.vintrello.com/

The second image i included is another logo design I liked and was thinking about using and decided I will probably also make a SECOND custom cut business card in the shape of that icon. Bonus if you can throw that in also.

Target Market(s)

Jewish consumers aged 20-35

Industry/Entity Type

Business

Contact Information for Business Card

see description.
Design should not be too crowded and should in eye-catching. Will mainly be used as fridge magnets.

Requirements
Must have
• Website address. logo.
Nice to have
• tagline. (The Definitive guide to kosher dining for the Kosher consumer)
• Im not a professional but I personally think the color blue goes along with this concept. ill leave it to you to decide.
Should not have
• any religious symbols.

```html
<!DOCTYPE html>
<html lang="en">
<head>
<meta charset="utf-8">
<title>PlateMarks business cards</title>
<link href="https://fonts.googleapis.com/css2?family=Open+Sans:wght@400;600&display=swap" rel="stylesheet">
<style>
  :root {
    --orange: #f07a2e;
    --orange-dark: #d9581f;
    --card: #f6f6f6;
    --card-edge: #e4e4e4;
    --ink: #222222;
    --muted: #555555;
    --backdrop: #d8d2ca;
  }
  * { box-sizing: border-box; margin: 0; padding: 0; }
  html, body { width: 1200px; height: 1023px; overflow: hidden; }
  body {
    background: var(--backdrop);
    font-family: "Open Sans", Arial, sans-serif;
    position: relative;
  }
  .card {
    position: absolute;
    left: 250px;
    width: 700px;
    height: 400px;
    background: linear-gradient(135deg, #ffffff 0%, var(--card) 60%, #ececec 100%);
    border-radius: 22px;
    box-shadow: 0 2px 0 var(--card-edge), 0 12px 28px rgba(0,0,0,0.18);
    overflow: hidden;
  }
  .card--front { top: 70px; }
  .card--back { top: 553px; }

  .brand {
    display: flex;
    align-items: center;
    gap: 18px;
    color: var(--orange);
    font-weight: 600;
  }
  .brand__dot {
    border-radius: 50%;
    background: var(--orange);
    flex: none;
  }
  .card--front .brand {
    position: absolute;
    left: 0; right: 0; top: 120px;
    justify-content: center;
    font-size: 74px;
    letter-spacing: -1px;
  }
  .card--front .brand__dot { width: 74px; height: 74px; }

  .tagline-band {
    position: absolute;
    left: 0; right: 0; bottom: 0;
    height: 62px;
    background: linear-gradient(180deg, var(--orange) 0%, var(--orange-dark) 100%);
    color: #ffffff;
    font-size: 22px;
    display: flex;
    align-items: center;
    justify-content: center;
    letter-spacing: 0.3px;
  }

  .card--back .brand {
    position: absolute;
    left: 70px; top: 80px;
    font-size: 46px;
    letter-spacing: -0.5px;
  }
  .card--back .brand__dot { width: 44px; height: 44px; }
  .divider {
    position: absolute;
    left: 70px; right: 70px; top: 190px;
    height: 2px;
    background: var(--orange);
  }
  .person {
    position: absolute;
    left: 70px; top: 212px;
  }
  .person__name { color: var(--orange); font-size: 26px; line-height: 1.2; }
  .person__title { color: var(--ink); font-size: 17px; line-height: 1.4; }
  .contacts {
    position: absolute;
    left: 330px; top: 214px;
    list-style: none;
    font-size: 16px;
    color: var(--muted);
  }
  .contacts li {
    display: flex;
    align-items: center;
    gap: 12px;
    height: 32px;
  }
  .contacts svg { width: 16px; height: 16px; flex: none; }
</style>
</head>
<body>
  <section class="card card--front" aria-label="Card front">
    <div class="brand"><span class="brand__dot"></span><span class="brand__name">PlateMarks</span></div>
    <div class="tagline-band">The Definitive guide to kosher dining for the Kosher consumer</div>
  </section>

  <section class="card card--back" aria-label="Card back">
    <div class="brand"><span class="brand__dot"></span><span class="brand__name">PlateMarks</span></div>
    <div class="divider"></div>
    <div class="person">
      <div class="person__name">Your Name</div>
      <div class="person__title">Title</div>
    </div>
    <ul class="contacts">
      <li>
        <svg viewBox="0 0 16 16"><path d="M8 1a5 5 0 0 1 5 5c0 4-5 9-5 9S3 10 3 6a5 5 0 0 1 5-5z" fill="#e8452c"/><circle cx="8" cy="6" r="2" fill="#fff"/></svg>
        Your address
      </li>
      <li>
        <svg viewBox="0 0 16 16"><circle cx="8" cy="8" r="7" fill="none" stroke="#e8452c" stroke-width="1.4"/><path d="M5.5 5c0 3 2.5 5.5 5.5 5.5l.5-1.5-1.7-.8-.8.8C7.9 8.6 7.4 8 7 6.9l.8-.8L7 4.5z" fill="#e8452c"/></svg>
        (123)123-456
      </li>
      <li>
        <svg viewBox="0 0 16 16"><rect x="1.5" y="3.5" width="13" height="9" fill="none" stroke="#e8452c" stroke-width="1.3"/><path d="M1.5 3.5 8 9l6.5-5.5" fill="none" stroke="#e8452c" stroke-width="1.3"/></svg>
        info@restaurant.vintrello.com
      </li>
      <li>
        <svg viewBox="0 0 16 16"><circle cx="8" cy="8" r="6.5" fill="none" stroke="#e8452c" stroke-width="1.3"/><ellipse cx="8" cy="8" rx="3" ry="6.5" fill="none" stroke="#e8452c" stroke-width="1.1"/><path d="M1.5 8h13" stroke="#e8452c" stroke-width="1.1"/></svg>
        www.restaurant.vintrello.com
      </li>
    </ul>
  </section>
</body>
</html>
```